K & T Fabrication Web Design | ||
Web Template | ||
Manufacturing | ||
www.kandtfab.example | ||
The current business that I am purchasing is a run of the mill, precision metal machining and manufacturing company. The owner is retirement age and it's my objective to make it new school and cutting edge. I want professional, eye catching concepts that capture what I am trying to do with the traditionally old school industry. I want to appeal to the younger engineers in the industry. I want to illustrate the professional, cutting edge services I intend to offer through my company. I want to show that we are not the traditional, dirty old machine shop. We are a company run by a young, fast-paced engineer focused on providing the highest quality work in the industry. | ||
I would like to have a navigation bar that contains "HOME", "CAPABILITIES", "PROJECTS", "ABOUT US", and "CONTACT US" tabs. I like un-cluttered websites that deliver a clear message that the company has an organized, structured leadership in place. I want to show that the machining industry is not always old, dirty, and antiquated. My company is cutting edge, engineering driven, and able to meet the customer's every demand. | ||
Cutting-Edge Unique/Creative Clean/Simple Professional Sophisticated Modern Industrial Progressive High Tech Masculine |
Black/Charcoal | ||
above header | ||
http://www.pellworth-clinical.example/ | ||
http://world.varnick-ostley.example/master/6600.htm | ||
http://brockmoorlifts.example/ | ||
Please attempt to match font type of the uploaded business card and company logo designs. I would like to have a seamless design throughout. | ||

```html
<!DOCTYPE html>
<html lang="en">
<head>
<meta charset="utf-8">
<title>K &amp; T Fabrication</title>
<link href="https://fonts.googleapis.com/css2?family=Arimo:wght@400;700&family=Roboto+Condensed:wght@400;700&display=swap" rel="stylesheet">
<style>
:root{
  --page:#ffffff;
  --charcoal:#2b2c30;
  --charcoal-dark:#1d1e21;
  --grey-text:#5b5b5b;
  --blue:#1f7fc4;
  --blue-light:#3a9be0;
  --blue-dark:#0f5f9c;
  --panel:#f1f1f1;
  --line:#d4d4d4;
  --white:#ffffff;
  --accent:#8fc6ef;
}
*{box-sizing:border-box;margin:0;padding:0}
html,body{width:1200px;height:1042px;overflow:hidden;background:var(--page);font-family:"Arimo",Arial,sans-serif;color:var(--grey-text)}
.canvas{position:relative;width:1200px;height:1042px}
.abs{position:absolute}

/* header */
.brand{left:30px;top:14px;display:flex;flex-direction:column;align-items:flex-start}
.brand-mark{width:74px;height:74px;border-radius:50%;background:#8c8f94;margin-left:58px}
.brand-name{margin-top:12px;font-size:34px;font-weight:700;color:var(--charcoal);letter-spacing:1px}
.brand-tag{margin-top:4px;font-size:11px;color:var(--grey-text);letter-spacing:1.5px;text-transform:uppercase}

.nav{left:14px;top:165px;width:894px;height:42px;background:linear-gradient(var(--blue-light),var(--blue-dark));border-radius:6px 6px 0 0;display:flex}
.nav a{flex:0 0 auto;display:block;color:var(--white);text-decoration:none;font-size:18px;line-height:42px;text-align:center}
.nav .item{width:180px}
.nav .active{background:var(--charcoal);}
.phone{left:970px;top:166px;display:flex;align-items:center;gap:12px;font-size:27px;color:var(--charcoal)}

.dropdown{left:530px;top:207px;width:205px;background:var(--charcoal);z-index:3;padding:4px 0}
.dropdown a{display:block;color:var(--white);font-size:14px;padding:6px 12px;text-decoration:none;border-bottom:1px solid #45474c}
.dropdown a:last-child{border-bottom:none}

/* hero */
.hero{left:14px;top:207px;width:1178px;height:276px;background:linear-gradient(90deg,#3a3c41 0%,#55575c 45%,#8d9095 100%);overflow:hidden}
.hero-photo{position:absolute;right:0;top:0;width:380px;height:276px;background:linear-gradient(180deg,#dfe3e7,#a9b0b7)}
.hero-title{position:absolute;left:22px;top:30px;font-family:"Roboto Condensed",Arial,sans-serif;font-size:44px;font-weight:700;color:var(--white)}
.hero-list{position:absolute;left:44px;top:96px;border-left:4px solid var(--white);padding-left:14px;font-family:"Roboto Condensed",Arial,sans-serif;font-size:34px;color:var(--white);line-height:46px}
.hero-dots{position:absolute;right:20px;bottom:40px;display:flex;gap:10px}
.hero-dots span{width:11px;height:11px;border-radius:50%;background:var(--white);opacity:.6}
.hero-dots span:first-child{opacity:1}

.brief{left:14px;top:483px;width:1178px;height:127px;background:linear-gradient(var(--blue),var(--blue-dark));padding:14px 20px;color:var(--white)}
.brief h2{font-family:"Roboto Condensed",Arial,sans-serif;font-size:30px;font-weight:400;margin-bottom:8px}
.brief p{font-size:14px;font-weight:700;line-height:19px}

/* columns */
.col{top:630px;height:273px;background:var(--panel);border:1px solid var(--line)}
.col-head{height:40px;background:linear-gradient(#ffffff,#e4e4e4);border-bottom:1px solid var(--line);display:flex;align-items:center;gap:10px;padding-left:14px;font-family:"Roboto Condensed",Arial,sans-serif;font-size:24px;color:var(--charcoal)}
.verticals{left:14px;width:300px}
.verticals ul{list-style:none;padding:10px 14px}
.verticals li{font-size:15px;padding:5px 0;border-bottom:1px solid var(--line)}
.spotlight{left:334px;width:272px}
.spotlight p{font-size:14px;padding:14px 16px 14px;border-bottom:1px solid var(--line);line-height:20px}
.showcase{left:624px;width:278px}
.showcase p{font-size:14px;padding:12px 14px;line-height:20px}
.showcase-photo{position:absolute;left:14px;bottom:14px;width:250px;height:120px;border-radius:6px;background:radial-gradient(circle at 30% 50%,#f2a640,#6b4a35 55%,#3a3a3c)}
.visit{position:absolute;right:20px;bottom:22px;background:var(--blue);color:var(--white);font-size:15px;font-weight:700;padding:6px 14px;border-radius:14px;border:2px solid var(--white)}

.testimonials{left:935px;top:630px;width:257px}
.testimonials h3{font-family:"Roboto Condensed",Arial,sans-serif;font-size:26px;font-weight:400;color:var(--charcoal);display:flex;justify-content:space-between;align-items:center}
.quote{margin-top:14px;border-top:1px solid var(--line);padding-top:10px;font-size:14px;line-height:19px}
.quote cite{display:block;text-align:right;font-style:normal;font-weight:700;color:var(--blue)}

/* footer */
.footer{left:14px;top:917px;width:1178px;height:125px;background:linear-gradient(var(--charcoal),var(--charcoal-dark));color:var(--white);padding:14px 20px}
.footer .contact{font-size:16px;font-weight:700}
.footer .contact span{font-weight:400;color:var(--accent);font-size:15px}
.footer .company{font-size:13px;margin-top:12px}
.footer .legal{font-size:13px;margin-top:8px}
.social{position:absolute;right:20px;top:46px;display:flex;align-items:center;gap:14px}
.social strong{font-family:"Roboto Condensed",Arial,sans-serif;font-size:22px;margin-right:6px}
.social span{width:44px;height:44px;border-radius:50%;background:#5a6b80}
</style>
</head>
<body>
<div class="canvas">

  <header>
    <div class="abs brand">
      <span class="brand-mark"></span>
      <span class="brand-name">K &amp; T FABRICATION</span>
      <span class="brand-tag">Precision products and engineered solutions</span>
    </div>

    <nav class="abs nav">
      <a class="item" href="#">home</a>
      <a class="item" href="#">capabilities</a>
      <a class="item" href="#">projects</a>
      <a class="item active" href="#">about us</a>
      <a class="item" href="#">contact us</a>
    </nav>

    <div class="abs phone">
      <svg width="26" height="30" viewBox="0 0 26 30"><path d="M6 2 L11 8 L8 12 Q11 19 16 22 L20 19 L25 25 L21 29 Q12 29 6 20 Q1 12 2 6 Z" fill="#2b2c30"/></svg>
      (555) 014-2870
    </div>

    <div class="abs dropdown">
      <a href="#">K&amp;T Fabrication</a>
      <a href="#">Tools and Trade</a>
      <a href="#">Industrial products</a>
    </div>
  </header>

  <section class="abs hero">
    <div class="hero-photo" role="img" aria-label="Photo of an engineer in a white hard hat"></div>
    <h1 class="hero-title">A specialized company in</h1>
    <div class="hero-list">Custom prototyping<br>Tool &amp; Die<br>Welding &amp; Automated assembly</div>
    <div class="hero-dots"><span></span><span></span><span></span></div>
  </section>

  <section class="abs brief">
    <h2>A brief</h2>
    <p>We are a turn-key shop that provides precision products and engineered solutions. We specialize in custom prototyping, tool and die, welding and automated assembly. We are a turn-key shop that provides precision products and engineered solutions. We specialize in custom prototyping, tool and die, welding and automated assembly.</p>
  </section>

  <section class="abs col verticals">
    <div class="col-head">
      <svg width="20" height="18" viewBox="0 0 20 18"><rect x="1" y="8" width="4" height="10" fill="#2b2c30"/><rect x="8" y="3" width="4" height="15" fill="#2b2c30"/><rect x="15" y="0" width="4" height="18" fill="#2b2c30"/></svg>
      Our verticals
    </div>
    <ul>
      <li>Custom prototyping</li>
      <li>Tool and Die</li>
      <li>Heavy weldings</li>
      <li>Automated assembly</li>
      <li>More services if any</li>
      <li>More services if any</li>
      <li>More services if any</li>
    </ul>
  </section>

  <section class="abs col spotlight">
    <div class="col-head">
      <svg width="20" height="20" viewBox="0 0 20 20"><polygon points="10,1 12.6,7 19,7.4 14,11.6 15.6,18.6 10,15 4.4,18.6 6,11.6 1,7.4 7.4,7" fill="#2b2c30"/></svg>
      Spotlight
    </div>
    <p>K&amp;T fabrication has completed with new tools and research.</p>
    <p>K&amp;T fabrication has completed with new tools and research.</p>
    <p>K&amp;T fabrication has completed with new tools and research.</p>
  </section>

  <section class="abs col showcase">
    <div class="col-head">
      <svg width="20" height="18" viewBox="0 0 20 18"><rect x="1" y="3" width="18" height="14" fill="none" stroke="#2b2c30" stroke-width="2"/><polyline points="3,15 8,9 12,13 14,11 17,15" fill="none" stroke="#2b2c30" stroke-width="2"/></svg>
      Showcase
    </div>
    <p>50 years of extensive engineering experience . We've done a great and respectful job to our satisfied clientel.</p>
    <div class="showcase-photo" role="img" aria-label="Photo of a gear being ground with sparks flying"></div>
    <span class="visit">Click to visit</span>
  </section>

  <section class="abs testimonials">
    <h3>Testimonials
      <svg width="24" height="22" viewBox="0 0 24 22"><path d="M2 2 H22 V15 H10 L5 20 V15 H2 Z" fill="none" stroke="#2b2c30" stroke-width="2"/></svg>
    </h3>
    <div class="quote">"The team demonstrated good technical expertise. Project Management is excellent."<cite>Dale, XYZ</cite></div>
    <div class="quote">"The team demonstrated good technical expertise. Project Management is excellent."<cite>Dale, XYZ</cite></div>
  </section>

  <footer class="abs footer">
    <div class="contact">CONTACT US &nbsp;<span>Email:info@kandtfab.example , Telephone: 999-999-9999 , Fax: 999-999-9999</span></div>
    <div class="company">K&amp;T Fabrication, Inc.</div>
    <div class="legal">© 2011-12 &nbsp;K&amp;T Fabrication. Sitemap | Privacy Policy | Disclaimer | Resources</div>
    <div class="social"><strong>GET SOCIAL WITH US</strong><span></span><span></span><span></span></div>
  </footer>

</div>
</body>
</html>
```